Raw Food & Health Coach Needs a Clutch Coupon

I need a clutch coupon for a raw food & health coaching business based in Washington, DC called Maren Okafor, LLC. I help ladies and gents on the go who want to support their bodies to stay healthy or prevent/correct disease so they can live extraordinary lives while deeply serving the world. My services include individual coaching, (online) group coaching, and corporate wellness coaching.

I would like to create a clutch coupon to give to referral partners who in turn will give them to their clients. So far I have two referral partners in mind: Tobias Venn Salon & Spa; and Colon Hydrotherapist Greta Mulvane.

Tobias Venn Salon & Spa will be having an event on Thursday, September 12, 2013, during which time their clients who get a hair cut will receive a complimentary Plumetra (hair) Treatment & a complimentary Radiant Roots Forward Blueprint Session with me.

I would like to see designs that use 2-4 colors, including a bit of green. The final design should communicate beauty/health from the inside out and boundless energy to enjoy an extraordinary life. It should be natural yet elegant/classy.

Designers are currently working on my business logo. The logo design project has not yet been completed. Once it completes, I will send the logo design to you and request that you incorporate the logo into your coupon design.

IMPORTANT: I need to select a winning design on Wed, Sept 11, 2013, and get the source files from the designer within 24 hours (before Thursday, Sept 12 MORNING); so that I have time to adjust any text and take it to the printer in order to distribute the coupon later that afternoon. I will need the source files urgently (within the next 24 hours).

Then after the event the designer will make the changes on the design for me incorporating my logo for use with multiple referral partners. I will approve the Payment when I have finalized the design

To repeat, I must have the winning design on September 11 (or Sept 12 morning at the latest).

IMPORTANT: Refer to uploaded Referral Partner Clutch Coupon SAMPLE to give you an idea of the layout I'd like, but PLEASE don't let it stifle YOUR creativity.
Updates

The focus should be on the Free Radiant Roots Forward Blueprint Session, not on me.

 

I think I’d prefer a white background and black text, unless you can convince me otherwise by showing me a beautiful design.

 

Ensure there is space between paragraphs.

 

Somehow differentiate my free gift (Vital Shield Starter Kit), phone and URL at the bottom on the back. While it would be nice to include my free gift, I may have to leave out if it won’t fit on the coupon.

Reason: Not completely satisfied yet and open to more designs. Maren

Reason: Need more time and would like to see more designs.

Target Market(s)

The audience is busy, heart-centered/socially responsible professional men and women on the go who hardly have time for self-care, but who will pay for holistic services (alternative therapies) to enhance their beauty/health so that they can perform their best while deeply serving the world without getting sick or having to endure toxic therapies like surgery, chemotherapy, radiation, and pills.

Industry/Entity Type

Printer

Requirements
Must have
• 2-4 colors, including a little green

Dimensions: approx. 2.25 inches x 5.25 inches.

Text from the uploaded file. Note: I'm not sure if all the text I've provided will fit nicely on the back of the coupon. If no then please increase the dimensions as little as possible.

The front of the coupon designed horizontally, and the back designed vertically.
Nice to have
• I'm open to your using illustrations or photos of the raw food and/or lifestyle tools that I use with clients in my business, such as green juice, (leafy) green veggies, cucumbers, lemons, berries, green smoothies, superfoods, movement/exercise, self-care...

I also like the idea of including a face in the design. When I’ve surveyed in the past people have related better to a face than just to a bowl of veggies or fruit.
Should not have
• the colors orange or red, or florescent colors.

```html
<!DOCTYPE html>
<html lang="en">
<head>
<meta charset="utf-8">
<title>Maren Okafor – Clutch Coupon</title>
<link rel="stylesheet" href="https://fonts.googleapis.com/css2?family=Cinzel:wght@400;600&family=Arimo:wght@400;700&family=Open+Sans:wght@300;400;500&display=swap">
<style>
  :root {
    --stage: #000000;
    --blush: #f8d7e6;
    --blush-light: #fdf0f6;
    --ink: #2b2b2b;
    --ink-soft: #555555;
    --muted: #8a8a8a;
    --magenta: #e0218a;
    --qa-tint: rgba(231, 120, 170, 0.35);
    --stone-dark: #3c3c3c;
    --stone-mid: #5d5d5d;
    --orchid: #c9519c;
    --gold: #d9a440;
    --white: #ffffff;
    --box-line: #d9c3cf;
  }
  * { box-sizing: border-box; margin: 0; padding: 0; }
  html, body { width: 1200px; height: 1000px; overflow: hidden; background: var(--stage); }
  .canvas { position: relative; width: 1200px; height: 1000px; }

  /* ---------- Back of coupon ---------- */
  .coupon-back {
    position: absolute; left: 52px; top: 116px; width: 320px; height: 746px;
    border-radius: 8px; overflow: hidden;
    background: radial-gradient(ellipse 70% 55% at 50% 48%, var(--white) 0%, var(--blush-light) 55%, var(--blush) 100%);
    font-family: "Arimo", Arial, sans-serif; color: var(--ink);
    padding: 20px 25px 0 26px;
  }
  .qa-mark {
    position: absolute; left: 44px; top: 0; font-family: "Cinzel", serif;
    font-size: 96px; color: var(--qa-tint); line-height: 1; letter-spacing: -4px;
  }
  .back-title {
    position: relative; font-family: "Cinzel", serif; font-weight: 600;
    font-size: 21px; line-height: 23px; text-align: center; color: #3a3a3a; margin-bottom: 4px;
  }
  .back-body p { position: relative; font-size: 9.3px; line-height: 12px; margin-bottom: 11px; }
  .back-body h3 { font-size: 11px; font-weight: 700; line-height: 12px; }
  .back-body .lead { font-weight: 700; margin-bottom: 0; }
  .benefit-list { list-style: none; font-size: 9.3px; line-height: 12px; padding-left: 12px; margin-bottom: 11px; }
  .benefit-list li::before { content: "• "; }

  .booking-row { display: flex; align-items: flex-start; gap: 12px; margin-top: 4px; padding-left: 17px; }
  .coach-portrait {
    width: 63px; height: 75px; flex: none; border: 2px solid var(--white);
    box-shadow: 0 0 2px rgba(0,0,0,.4);
    background: linear-gradient(160deg, #7a4b35, #c89a7e 55%, #4a2c22);
  }
  .booking-text { font-family: "Open Sans", sans-serif; font-weight: 400; font-size: 11.5px; line-height: 15px; color: var(--muted); padding-top: 12px; }
  .booking-text a { color: var(--magenta); text-decoration: none; }

  .gift-box {
    margin: 16px 2px 0 3px; border: 1px solid var(--box-line); border-radius: 8px;
    background: rgba(255,255,255,.35); text-align: center; padding: 5px 4px 6px;
  }
  .gift-box h4 { font-size: 11.5px; font-weight: 700; color: #3a3a3a; line-height: 14px; }
  .gift-box p { font-size: 8.6px; font-weight: 700; line-height: 13px; color: #333; }

  /* ---------- Front of coupon ---------- */
  .coupon-front {
    position: absolute; left: 402px; top: 319px; width: 748px; height: 320px;
    border-radius: 8px; overflow: hidden;
    background: radial-gradient(ellipse 45% 70% at 78% 50%, var(--white) 0%, var(--blush-light) 55%, var(--blush) 100%);
  }
  .front-art { position: absolute; left: 0; top: 0; }
  .brand-name {
    position: absolute; left: 158px; top: 72px; font-family: "Cinzel", serif;
    font-size: 24px; letter-spacing: 1px; color: var(--white);
  }
  .brand-role {
    position: absolute; left: 158px; top: 102px; width: 244px; padding-bottom: 9px;
    font-family: "Open Sans", sans-serif; font-size: 10px; color: var(--white);
    border-bottom: 1px solid var(--white);
  }
  .offer-title {
    position: absolute; left: 154px; top: 137px; width: 290px;
    font-family: "Open Sans", sans-serif; font-weight: 500; font-size: 23px; line-height: 30px; color: var(--white);
  }
  .offer-value {
    position: absolute; left: 504px; top: 46px; font-family: "Open Sans", sans-serif;
    font-weight: 300; font-size: 18.5px; line-height: 24px; color: #444;
  }
  .offer-booking {
    position: absolute; left: 506px; top: 145px; font-family: "Open Sans", sans-serif;
    font-size: 13.5px; line-height: 17px; color: var(--muted);
  }
  .offer-booking a { color: var(--magenta); text-decoration: none; }
  .partner-label {
    position: absolute; left: 506px; top: 221px; font-family: "Open Sans", sans-serif;
    font-size: 11px; color: var(--muted);
  }
  .partner-name {
    position: absolute; left: 506px; top: 242px; width: 110px;
    font-family: "Open Sans", sans-serif; font-size: 13px; line-height: 17px; color: var(--ink-soft);
  }
</style>
</head>
<body>
<main class="canvas">

  <section class="coupon-back">
    <div class="qa-mark" aria-hidden="true">Q&amp;A</div>
    <h2 class="back-title">What is raw food &amp;<br>health coaching?</h2>
    <div class="back-body">
      <p>Raw food coaching helps you go or stay raw to the level that you truly desire.</p>
      <p>Health couching helps you connect the dots between what you eat and how you feel. You'll know how to detoxify your body, boost your immune system, multiply your energy, improve your mood, gravitate to the perfect body weight for you, and delight in what you eat like never before – without restriction.</p>
      <h3>Who benefits from this work?</h3>
      <p>Ladies and gents on the go who want to enable their bodies to prevent or correct disease and create abundant energy so they can live extraordinary lives while deeply serving the world.</p>
      <p>Raw food is literally for everyone, but the degree to which someone goes raw and for what duration is a very personal decision. This is about what works for you, what feels right for you and what get you to where you want to be.</p>
      <p class="lead">Generally speaking, raw food is great for anyone who wants to…</p>
      <ul class="benefit-list">
        <li>Correct or prevent a serious disease</li>
        <li>Look and/or feel better</li>
        <li>Look/feel 10 years younger</li>
        <li>Fit into their skinny jeans without dieting</li>
        <li>Double their energy</li>
        <li>Reduce their cravings</li>
        <li>Detox their body</li>
        <li>Think more clearly</li>
        <li>Get a lot done without having a lot of time</li>
        <li>Feel happier</li>
      </ul>
      <p class="lead">What happens in the initial strategy session?</p>
      <p>This 30 minute phone call is a time to discuss your unique health challenge(s) and desires. I guarantee you'll walk away with at least 1 aha about why you're stuck and more clarity about what it'll take to put you on the fast track to where you want to go.</p>
    </div>
    <div class="booking-row">
      <div class="coach-portrait" role="img" aria-label="Portrait photo of the coach"></div>
      <p class="booking-text">To book your complimentary<br>strategy session<br>simply go to: <a href="#">http://bit.ly/RRfBx</a></p>
    </div>
    <div class="gift-box">
      <h4>Afraid of getting cancer?</h4>
      <p>Decide To Get Healthy Because It's Time…<br>Get Your Free Vital Shield Starter Kit At<br>Marenokafor.com TODAY!</p>
    </div>
  </section>

  <section class="coupon-front">
    <svg class="front-art" width="470" height="320" viewBox="0 0 470 320">
      <defs>
        <radialGradient id="stones" cx="35%" cy="55%" r="75%">
          <stop offset="0" stop-color="var(--stone-mid)"/>
          <stop offset="1" stop-color="var(--stone-dark)"/>
        </radialGradient>
        <radialGradient id="orchids" cx="0" cy="0" r="1" gradientUnits="userSpaceOnUse" gradientTransform="translate(60 40) scale(190 150)">
          <stop offset="0" stop-color="var(--orchid)"/>
          <stop offset="0.55" stop-color="var(--orchid)" stop-opacity="0.55"/>
          <stop offset="1" stop-color="var(--orchid)" stop-opacity="0"/>
        </radialGradient>
      </defs>
      <g role="img" aria-label="Photo of pink orchids on smooth black spa stones">
        <path d="M0 0 H420 Q470 160 420 320 H0 Z" fill="url(#stones)"/>
        <path d="M0 0 H420 Q470 160 420 320 H0 Z" fill="url(#orchids)"/>
      </g>
      <path d="M420 0 Q470 160 420 320 L438 320 Q488 160 438 0 Z" fill="var(--gold)"/>
    </svg>
    <div class="brand-name">MAREN OKAFOR</div>
    <div class="brand-role">RAW FOOD &amp; HEALTH COACH</div>
    <h1 class="offer-title">Free Radiant Roots Forward Blueprint Session with Certified Raw Food &amp; Health Coach</h1>
    <p class="offer-value">30 minutes focused<br>entirely on you<br>(a $50 value, free)</p>
    <p class="offer-booking">To book your complimentary<br>strategy session<br>simply go to: <a href="#">http://bit.ly/RRfBx</a></p>
    <p class="partner-label">Compliments Of</p>
    <p class="partner-name">Tobias Venn Salon &amp; Spa</p>
  </section>

</main>
</body>
</html>
```